Geschäftspapiere für Fliesenleger - Meisterbetrieb
Zielgruppe
Wir sind ein mittelständischer Fliesenleger - Meisterbetrieb und möchten unsere Geschäftspapiere erneuern. Unsere Kunden sind Privatkunden, Gewerbetreibende sowie Öffentliche Auftraggeber.
Aufgabenstellung
Unser Logo stellen wir Ihnen zur verfügung und soll unverändert bleiben.
Wir benötigen folgende Geschäftspapiere:
- Briefpapier DIN A4
- Notizblock Karriert DIN A4
- Visitenkarten 5,5 x 8,5 cm
- Kuvert DIN lang mit Fenster
- Kuvert DIN C4 mit Fenster
Bei der Farbe Rot handelt es sich um Verkehrsrot RAL 3020
Als Schriftart haben wir uns Helvetica Neue vorgestellt.
Wir bitten jedoch auch um Vorschläge anderer Moderner und gut lesbarer Schriftarten die für Print und Web bestens geeignet sind.
Wir wünschen uns ein Modernes und Schnörkelloses Design. Bei den Dateien habe ich Ihnen ein Stockphoto angehängt um Ihnen zu zeigen wie wir uns ein Cover oder eine Broschüre vorstellen können. Nur um Ihnen unsere Ideen / Vorstellungen näher zu bringen.

```html
<!DOCTYPE html>
<html lang="de">
<head>
<meta charset="utf-8">
<title>Briefpapier Fliesen-Kelmor</title>
<link rel="stylesheet" href="https://fonts.googleapis.com/css2?family=Inter:wght@400;700;800&display=swap">
<style>
  :root {
    --bg: #ffffff;
    --paper: #ffffff;
    --red: #e30b1c;
    --red-dark: #a8111e;
    --red-deep: #7d0f17;
    --ink: #111111;
    --footer-text: #f6dede;
  }
  html, body {
    margin: 0;
    width: 1200px;
    height: 1200px;
    overflow: hidden;
    background: var(--bg);
    font-family: "Inter", "Helvetica Neue", Arial, sans-serif;
  }
  .letterhead {
    position: absolute;
    left: 325px;
    top: 163px;
    width: 595px;
    height: 843px;
    background: var(--paper);
    overflow: hidden;
  }
  .letterhead__shapes {
    position: absolute;
    inset: 0;
    width: 595px;
    height: 843px;
  }
  .brand-name {
    position: absolute;
    left: 21px;
    top: 84px;
    margin: 0;
    font-size: 31px;
    font-weight: 800;
    letter-spacing: -0.5px;
    color: var(--ink);
    line-height: 1;
  }
  .sender {
    position: absolute;
    left: 286px;
    top: 22px;
    margin: 0;
    font-size: 9.6px;
    line-height: 12px;
    color: var(--red);
    font-style: normal;
  }
  .sender__company { font-weight: 700; }
  .sender__gap { height: 12px; }
  .footer-info {
    position: absolute;
    inset: 0;
    font-size: 9.4px;
    line-height: 12px;
    color: var(--footer-text);
  }
  .footer-info span {
    position: absolute;
    white-space: nowrap;
  }
</style>
</head>
<body>
  <main class="letterhead">
    <svg class="letterhead__shapes" viewBox="0 0 595 843" aria-hidden="false">
      <defs>
        <linearGradient id="interior-tones" x1="0" y1="0" x2="1" y2="1">
          <stop offset="0" stop-color="#d9d6d1"/>
          <stop offset="0.5" stop-color="#9b8f88"/>
          <stop offset="1" stop-color="#5f5b58"/>
        </linearGradient>
        <linearGradient id="worker-tones" x1="0" y1="0" x2="1" y2="1">
          <stop offset="0" stop-color="#e8c57a"/>
          <stop offset="0.5" stop-color="#e2a634"/>
          <stop offset="1" stop-color="#b07a4e"/>
        </linearGradient>
      </defs>

      <!-- top right corner -->
      <polygon class="band band--red" fill="var(--red)" points="392,47 440,0 595,0 595,272"/>
      <polygon class="band band--dark" fill="var(--red-dark)" points="440,0 500,0 440,47 425,33"/>
      <polygon class="photo" role="img" aria-label="Foto eines modernen Wohnraums mit Sofa und gefliestem Boden" fill="url(#interior-tones)" points="500,0 595,0 595,228 442,50"/>

      <!-- bottom left corner -->
      <polygon class="band band--red" fill="var(--red)" points="0,487 252,735 150,843 0,843"/>
      <polygon class="photo" role="img" aria-label="Foto einer Hand mit gelbem Arbeitshandschuh vor einer Baustelle" fill="url(#worker-tones)" points="0,555 0,843 105,843 205,745"/>
      <polygon class="band band--dark" fill="var(--red-dark)" points="205,745 232,745 136,843 105,843"/>

      <!-- footer band -->
      <polygon class="footer-band" fill="var(--red-dark)" points="272,740 595,740 595,843 170,843"/>
    </svg>

    <h1 class="brand-name">Fliesen-Kelmor</h1>

    <address class="sender">
      <div class="sender__company">KLMR Kelmor GmbH</div>
      <div>Unterwaldbach 14</div>
      <div>91234 Talhausen</div>
      <div class="sender__gap"></div>
      <div>Tel : 09123-4567810</div>
      <div>Fax: 09123-4567899</div>
      <div>post@fliesen-kelmor.de</div>
      <div>www.fliesen-kelmor.de</div>
    </address>

    <div class="footer-info">
      <span style="left:280px;top:752px">Bankverbindung: Volksbank Talgrund</span>
      <span style="left:272px;top:765px">IBAN: DE00 0000 0000 0000 0000 00</span>
      <span style="left:262px;top:777px">BIC: GENODEX1TAL</span>
      <span style="left:240px;top:800px">Geschäftsführer: Tobias Kelmor · HRB 1234 Amtsgericht Talstadt</span>
      <span style="left:229px;top:813px">Ust. ID: DE000000000</span>
    </div>
  </main>
</body>
</html>
```